Website Design for Webflow platform

The existing website is tired and not enticing the reader by content or visuals or CTAs . The industry is serious and competitive and demands the business to relate to this audience. Use of graphics and video and sharp relatable imagery mixed in with content. Create an exciting professional progressive homepage design that keeps the visitor wanting to view the whole page. Create supplementary coordinated pages/templates for other pages for this new website. It should be memorable, not boring, but professional and command confidence in the business and services offered in this type of industry. This needs to be coded for Webflow platform
Updates

Target Market(s)

Emergency management professionals/decision makers from high risk industries - oil & gas, transporation airline/rail/water, government, community responders, police, fire, military, chemical, nuclear, utilities

Industry/Entity Type

Emergency management services for Industry, Big Business, Government, Education Facilities, Hospitals, Correctional Facilities, Banking, Insurance

Coding

Coded - Design and coding required

Number of Pages Required

5+ page

Font styles to use
Serif
Sans Serif
Other font styles liked:
• Ubuntu and Calibri - see Brand document attached

Colors
0094D4
00A9DD
6FCCEA
C7EBF8
E9F6FB
00AB8E
00BBA5
67D7C9
C6EFE9
E9F9F6
F0912C
F2A743
F7CA91
FBE8D2
FDF5EE
6B429C
8869AF
B7A5CE
E3DAEB
F3F0F8

Requirements
Must have
• A home page that links to other pages. Must be exciting design relative to the industry and utilize powerful images that portray the seriousness of the business
Nice to have
• Great calls to action related to the industry. Animations that are professional, not too busy but leading edge in the design and the content.
Should not have
• boring typical page layouts

```html
<!DOCTYPE html>
<html lang="en">
<head>
<meta charset="utf-8">
<title>Services – Ridgeline Consulting</title>
<link href="https://fonts.googleapis.com/css2?family=Ubuntu:wght@400;500;700&display=swap" rel="stylesheet">
<style>
:root{
  --blue:#0094D4;
  --blue-bright:#00A9DD;
  --blue-pale:#E9F6FB;
  --orange:#F0912C;
  --purple:#8869AF;
  --lilac-band:#F2EFF6;
  --ink:#2b2f36;
  --text:#4a4f57;
  --white:#ffffff;
  --footer:#1E8FD2;
}
*{box-sizing:border-box;margin:0;padding:0}
html,body{width:1200px;height:3746px;overflow:hidden}
body{position:relative;font-family:"Ubuntu",sans-serif;color:var(--text);background:var(--white);font-size:13px;line-height:1.62}
b{color:var(--ink);font-weight:500}
.abs{position:absolute}

/* hero */
.hero{left:0;top:0;width:1200px;height:390px;background:linear-gradient(180deg,#3a4650 0%,#55606a 40%,#2e3940 100%)}
.hero-photo{position:absolute;inset:0;background:radial-gradient(ellipse at 55% 30%,#6d747a 0%,#3b4148 45%,#1f2a30 100%)}
.hero-shade{position:absolute;inset:0;background:linear-gradient(90deg,rgba(20,30,40,.45),rgba(20,30,40,.15) 60%,rgba(20,30,40,.4))}
.brand{position:absolute;left:97px;top:48px;color:var(--white);font-weight:700;font-size:22px;letter-spacing:.5px;display:flex;align-items:center;gap:8px}
.brand .mark{width:14px;height:14px;background:var(--white)}
.nav{position:absolute;left:451px;top:56px;display:flex;gap:24px;color:var(--white);font-size:15px}
.nav span.drop::after{content:" \2304";font-size:10px}
.hero-rule{position:absolute;left:584px;top:175px;width:1px;height:109px;background:rgba(240,145,44,.6)}
.hero-title{position:absolute;left:633px;top:176px;color:var(--white);font-size:55px;font-weight:500;line-height:1}
.crumb{position:absolute;left:634px;top:253px;color:var(--orange);font-size:13px}

/* sidebar */
.sidebar{left:74px;top:463px;width:307px;height:714px;background:var(--blue-pale);border-radius:6px;padding:32px 26px}
.sidebar h3{font-size:27px;font-weight:500;color:var(--ink);margin-bottom:22px}
.svc{display:flex;justify-content:space-between;align-items:center;height:42px;background:var(--white);border-radius:3px;padding:0 16px;font-size:13px;color:var(--ink);margin-bottom:18.5px;box-shadow:0 1px 2px rgba(0,0,0,.04)}
.svc.active{background:var(--blue);color:var(--white)}
.svc::after{content:"\2192";color:var(--blue);font-size:14px}
.svc.active::after{color:var(--white)}

/* main column */
.main{left:438px;top:463px;width:686px}
.photo{border-radius:6px;width:100%}
.main .photo{height:322px;background:linear-gradient(120deg,#e9ebec 0%,#d6d9db 40%,#c8342c 55%,#b4241f 70%,#d9dcde 100%)}
h2{font-size:22px;font-weight:500;color:var(--ink);line-height:1.3}
.main h2{margin:26px 0 12px}
.main p{margin-bottom:12px}
.btn{display:inline-block;background:var(--orange);color:var(--white);font-weight:500;font-size:13px;border-radius:3px;text-align:center;line-height:44px}
.main .btn{width:361px;margin:8px 0 0}
.main h2.second{margin-top:30px}
.ticks{list-style:none;margin:18px 0 14px}
.ticks li{position:relative;padding-left:22px;margin-bottom:12px;padding-right:20px}
.ticks li::before{content:"";position:absolute;left:2px;top:5px;width:11px;height:11px;border-radius:50%;background:var(--blue)}
.ticks li::after{content:"";position:absolute;left:5px;top:8px;width:3px;height:3px;border-top:1.5px solid #fff;border-right:1.5px solid #fff;transform:rotate(45deg)}
.main .indent{padding-left:3px}

/* planning band */
.band{left:0;top:1580px;width:1200px;height:384px;background:var(--lilac-band);text-align:center;padding-top:52px}
.band h2{margin-bottom:14px}
.band p{width:900px;margin:0 auto 14px}
.band .btn{width:262px;margin-top:4px}

/* training */
.training{left:74px;top:2036px;width:1050px}
.training .photo{height:360px;background:linear-gradient(110deg,#6a5a4d 0%,#2fb3cf 35%,#8a6a55 50%,#2aaecd 70%,#c8cfd4 100%)}
.training h2{margin:36px 0 12px}
.training p{margin-bottom:14px}
.training h2.second{margin-top:18px;margin-bottom:18px}
.cards{position:absolute;top:793px;left:2px;display:flex;gap:18px}
.card{width:248px;height:221px;background:var(--purple);border-radius:3px;display:flex;flex-direction:column;align-items:center;padding-top:38px;color:var(--white);font-size:16px;font-weight:500}
.card .dot{width:88px;height:88px;border-radius:50%;background:var(--white);margin-bottom:18px}

/* footer */
.footer{left:0;top:3156px;width:1200px;height:590px;background:linear-gradient(160deg,#2497d8 0%,var(--footer) 60%,#1a86c8 100%);color:var(--white)}
.footer .brand-lg{position:absolute;left:0;width:1200px;top:70px;text-align:center;font-size:54px;font-weight:700}
.fcol{position:absolute;top:198px;font-size:14px}
.fcol h4{font-size:14px;font-weight:500;margin-bottom:10px;letter-spacing:.3px}
.fcol ul{list-style:none}
.fcol li{line-height:27px}
.fcol li::before{content:"\203A";margin-right:7px}
.contact-line{position:relative;padding-left:28px;margin-bottom:16px;line-height:22px}
.contact-line svg{position:absolute;left:0;top:3px}
.contact-line strong{font-weight:700}
.social{display:flex;align-items:center;gap:6px;font-weight:700;font-size:18px;margin-left:28px;margin-top:22px}
.social span.sq{width:16px;height:16px;background:var(--white)}
.copy{position:absolute;left:84px;top:551px;font-size:11px}
</style>
</head>
<body>

<header class="abs hero">
  <div class="hero-photo" role="img" aria-label="Aerial view of an industrial site under heavy dark smoke"></div>
  <div class="hero-shade"></div>
  <div class="brand"><span class="mark"></span>Ridgeline</div>
  <nav class="nav"><span>Home</span><span>About</span><span class="drop">Services</span><span class="drop">Courses</span><span>Blog</span><span>Contact</span></nav>
  <div class="hero-rule"></div>
  <h1 class="hero-title">Services</h1>
  <div class="crumb">Home » Services</div>
</header>

<aside class="abs sidebar">
  <h3>All Services</h3>
  <div class="svc active">Emergency Management</div>
  <div class="svc">Training &amp; Simulation Eventts</div>
  <div class="svc">Business Continuity Preparation</div>
  <div class="svc">Fire &amp; Life Safety</div>
  <div class="svc">Security Management</div>
  <div class="svc">ICS Certification</div>
  <div class="svc">Crisis Communication</div>
  <div class="svc">Leadership Development</div>
  <div class="svc">ICS Training &amp; Certification</div>
  <div class="svc">Contractor Safety</div>
</aside>

<main class="abs main">
  <div class="photo" role="img" aria-label="Red fire extinguishers against a light wall"></div>
  <h2>Emergency Management: Are You Prepared?</h2>
  <p><b>Is your organization equipped with the essential emergency response planning tools, resources, and training to respond effectively to an emergency?</b> At Ridgeline Consulting, with decades of experience, we specialize in ensuring that organizations are not just prepared but are resilient in the face of crises.</p>
  <p><b>We offer comprehensive Emergency Management services, combining meticulous planning, business continuity expertise, and specialized instructor training</b> to make sure you're fully prepared for whatever challenges may come your way.</p>
  <span class="btn">Download our Emergency management brochure</span>
  <h2 class="second">Program Development: Strengthen Your Resilience</h2>
  <p>At Ridgeline Consulting, with decades of experience, we specialize in ensuring that organizations are not just prepared but are resilient in the face of crises.</p>
  <ul class="ticks">
    <li>Conducting a <b>Comprehensive Emergency Preparedness Audit</b> based on industry regulations, standards, and best practices.</li>
    <li><b>Developing Key Performance Indicators (KPIs)</b> to monitor your program's effectiveness.</li>
    <li><b>Crafting comprehensive documentation</b>, including standards, policies, and competency frameworks for regulatory compliance.</li>
    <li><b>Designing a training plan</b> using our instructor training expertise to build both capability and capacity.</li>
    <li><b>Creating an exercise plan</b> for ongoing validation and continuous improvement.</li>
  </ul>
  <p class="indent">In today's unpredictable environment, meeting company policy and operational risks with a well-rounded emergency management program is not a luxury but a necessity. <b>By partnering with us, you ensure that you're better prepared today for the uncertainties of tomorrow.</b></p>
  <p class="indent">Serving Calgary and Beyond in Emergency Management</p>
</main>

<section class="abs band">
  <h2>Emergency Planning: Your Blueprint for Safety</h2>
  <p><b>Effective planning is the cornerstone of emergency management.</b> At Ridgeline Consulting, we take pride in our ability to develop plans tailored to your organization's unique needs. Our planning process involves working with key stakeholders in, conducting a Hazard Identification and Risk Assessment, and ongoing reviews to ensure the highest quality.</p>
  <p>From <b>small enterprises to complex, multi-sector organizations</b>, we have experience in developing Emergency Response Plans, Crisis Management Plans, and Crisis Communication Plans that adhere to regulatory requirements and are built on best practices.</p>
  <p>Boost your disaster readiness now!</p>
  <span class="btn">Contact us for a Consultation</span>
</section>

<section class="abs training">
  <div class="photo" role="img" aria-label="Group of trainees in turquoise shirts attending a classroom session"></div>
  <h2>Training and Education: Where Knowledge Meets Practice</h2>
  <p><b>Training is our key strength at Ridgeline Consulting.</b> With our instructor training programs, we believe that a well-trained team is your best defense against emergencies. That's why <b>we offer some of the best training and exercise programs in North America.</b> Our courses are custom-designed to reflect the operational needs of your organization, led by our team of experts from diverse backgrounds including military, public safety, and healthcare.</p>
  <p><b>Our training modules</b> aim to help your team with the skills and knowledge they need to manage emergencies effectively:</p>
  <h2 class="second">Exercises and Validation: Test, Learn, Adapt</h2>
  <p>Looking to test your emergency response planning or business continuity strategy? Ridgeline Consulting offers a range of exercises designed to meet your specific needs. Our exercise programs are not just about identifying gaps; they're about ongoing learning and improvement.</p>
  <p>We take a <b>building-block approach to exercises, enabling teams to learn and grow in a controlled, safe environment</b>. Whether you're in utilities, oil and gas, municipalities, education, or food services, our exercises meet regulatory compliance standards and exceed your expectations.</p>
  <p><b>Through these exercises, your team gains practical experience, allowing them to apply theoretical knowledge in real-world settings</b>, thereby effectively mitigating operational risks.</p>
  <div class="cards">
    <div class="card"><span class="dot"></span>Walkthroughs</div>
    <div class="card"><span class="dot"></span>Tabletop Exercises</div>
    <div class="card"><span class="dot"></span>Functional Exercises</div>
    <div class="card"><span class="dot"></span>Full-Scale Exercises</div>
  </div>
</section>

<footer class="abs footer">
  <div class="brand-lg">Ridgeline</div>
  <div class="fcol" style="left:89px"><h4>QUICK LINKS</h4><ul><li>Home</li><li>About</li><li>Services</li><li>Courses</li><li>Blog</li><li>Contact</li></ul></div>
  <div class="fcol" style="left:297px"><h4>SERVICES</h4><ul><li>Emergency management</li><li>Business continuity</li><li>Leadership development</li><li>Safety &amp; contractor</li><li>management</li><li>Security management</li><li>Fire and life safety training</li><li>Beacon response app</li></ul></div>
  <div class="fcol" style="left:577px"><h4>COURSES</h4><ul><li>Certified ics courses</li><li>Ics aligned courses</li><li>Additional courses</li><li>Online courses</li><li>Course calendar</li><li>Book a course</li></ul></div>
  <div class="fcol" style="left:842px;top:200px">
    <h4>CONTACT US</h4>
    <div class="contact-line"><svg width="16" height="16" viewBox="0 0 24 24"><path d="M6.6 10.8a15 15 0 0 0 6.6 6.6l2.2-2.2a1 1 0 0 1 1-.25 11 11 0 0 0 3.6.6 1 1 0 0 1 1 1V20a1 1 0 0 1-1 1A17 17 0 0 1 3 4a1 1 0 0 1 1-1h3.5a1 1 0 0 1 1 1 11 11 0 0 0 .6 3.6 1 1 0 0 1-.25 1z" fill="#F2A743"/></svg>Phone: (403) 555-0148</div>
    <div class="contact-line"><svg width="14" height="18" viewBox="0 0 14 18"><path d="M7 0a7 7 0 0 0-7 7c0 5 7 11 7 11s7-6 7-11a7 7 0 0 0-7-7zm0 9.5A2.5 2.5 0 1 1 7 4.5a2.5 2.5 0 0 1 0 5z" fill="#F2A743"/></svg><strong>Head Office:</strong><br>Suite 1800, 212 9th Ave S.W.<br><strong>North Tower</strong><br>Calgary, Alberta, T2P 0A1</div>
    <div class="contact-line"><svg width="14" height="18" viewBox="0 0 14 18"><path d="M7 0a7 7 0 0 0-7 7c0 5 7 11 7 11s7-6 7-11a7 7 0 0 0-7-7zm0 9.5A2.5 2.5 0 1 1 7 4.5a2.5 2.5 0 0 1 0 5z" fill="#F2A743"/></svg><strong>Toronto Office:</strong><br>Suite 305, 88 Harbourview Rd.<br>Toronto, Ontario, M5J 0B2</div>
    <div class="social">Connectly<span class="sq"></span></div>
  </div>
  <div class="copy">© Ridgeline Consulting 2026 – All Rights Reserved</div>
</footer>

</body>
</html>
```